Medical Staffing Pamphlet

We are starting to staff for Medical positions for the first time, we need pamphlets to take to medical facilities to try to gain new business

Need an copy to edit, many errors.

```html
<!DOCTYPE html>
<html lang="en">
<head>
<meta charset="utf-8">
<title>Keystone Staffing Medical – Tri-fold Pamphlet</title>
<link rel="stylesheet" href="https://fonts.googleapis.com/css2?family=Open+Sans:wght@400;600;700&family=Arimo:wght@400&display=swap">
<style>
  :root{
    --page:#e4e6ea;
    --navy:#1f2f66;
    --blue:#5f7bb8;
    --blue-soft:#8ea4d3;
    --paper:#f1f3f7;
    --grey:#d3d6dc;
    --grey-dark:#b9bdc5;
    --green:#4fae3b;
    --white:#ffffff;
  }
  *{box-sizing:border-box;margin:0;padding:0}
  html,body{width:1200px;height:801px;overflow:hidden;background:var(--page)}
  body{font-family:"Open Sans",Arial,sans-serif;position:relative}

  .pamphlet{position:absolute;left:90px;top:75px;width:1020px;height:650px;display:flex;
    box-shadow:0 6px 24px rgba(0,0,0,.18)}
  .panel{position:relative;width:340px;height:650px;overflow:hidden}
  .panel + .panel{border-left:1px solid rgba(0,0,0,.08)}
  .panel svg.waves{position:absolute;inset:0;width:340px;height:650px}

  .photo{position:absolute}

  /* left panel */
  .panel--intro{background:var(--paper)}
  .photo--handshake{left:55px;top:35px;width:200px;height:200px;border-radius:50%;
    background:radial-gradient(circle at 55% 55%,#c9a58b 0%,#b7c4dc 45%,#e8ecf3 100%);
    border:5px solid var(--white)}
  .intro-statement{position:absolute;left:28px;top:300px;width:290px;color:var(--white);
    font-weight:600;font-size:16px;letter-spacing:3px;line-height:1.45;text-transform:uppercase}
  .photo--consult{left:0;top:455px;width:340px;height:195px;
    background:linear-gradient(135deg,#8ea0bb 0%,#d9dde4 45%,#f3f3f1 70%,#aab9cf 100%)}

  /* middle panel */
  .panel--contact{background:linear-gradient(180deg,#dfe1e5 0%,var(--grey) 100%)}
  .photo--doctor{left:40px;top:40px;width:260px;height:200px;
    background:linear-gradient(180deg,#d9dbe0 0%,#eef0f3 55%,#c6cad2 100%)}
  .contact{position:absolute;left:60px;top:285px;color:var(--white)}
  .contact h2{font-size:25px;font-weight:700;letter-spacing:.5px;margin-bottom:8px}
  .contact p{font-size:16px;line-height:1.5;opacity:.92}
  .program-title{position:absolute;left:0;right:0;top:505px;text-align:center;font-family:"Arimo",Arial,sans-serif}
  .program-title .name{display:block;font-size:24px;color:var(--navy)}
  .program-title .field{display:block;font-size:21px;color:var(--green);margin-top:2px}

  /* right panel */
  .panel--cover{background:var(--paper)}
  .photo--team{left:20px;top:30px;width:300px;height:215px;
    background:linear-gradient(180deg,#eef0f4 0%,#dfe4ee 50%,#c3cde0 100%)}
  .tagline{position:absolute;left:30px;right:30px;top:285px;text-align:center;color:var(--white);
    font-size:19px;font-weight:600;line-height:1.35}
  .brand{position:absolute;left:50px;top:500px;display:flex;align-items:center;gap:14px}
  .brand-mark{width:30px;height:30px;background:var(--navy)}
  .brand-name{font-weight:700;font-size:18px;line-height:1.2;color:var(--navy);text-transform:uppercase}
</style>
</head>
<body>
<main class="pamphlet">

  <section class="panel panel--intro">
    <svg class="waves" viewBox="0 0 340 650" aria-hidden="true">
      <path d="M0 120 C80 90 240 70 340 95 L340 110 C240 90 90 110 0 140 Z" fill="var(--navy)"/>
      <path d="M0 250 C90 220 230 230 340 255 L340 470 L0 470 Z" fill="var(--blue)"/>
      <path d="M0 255 C90 225 230 235 340 260 L340 272 C230 248 90 240 0 270 Z" fill="var(--navy)"/>
    </svg>
    <div class="photo photo--handshake" role="img" aria-label="Photo of a doctor shaking hands"></div>
    <p class="intro-statement">Our medical staffing specialists will provide you quality employees</p>
    <div class="photo photo--consult" role="img" aria-label="Photo of a doctor consulting with an older patient"></div>
  </section>

  <section class="panel panel--contact">
    <svg class="waves" viewBox="0 0 340 650" aria-hidden="true">
      <path d="M0 30 C100 25 230 15 340 0 L340 14 C230 30 100 40 0 44 Z" fill="var(--navy)"/>
      <path d="M0 240 C100 225 240 225 340 235 L340 470 C240 455 100 460 0 480 Z" fill="var(--blue)"/>
      <path d="M0 236 C100 222 240 222 340 231 L340 243 C240 234 100 234 0 250 Z" fill="var(--navy)"/>
    </svg>
    <div class="photo photo--doctor" role="img" aria-label="Photo of a smiling female doctor holding a clipboard"></div>
    <div class="contact">
      <h2>CONTACT US</h2>
      <p>2450 N. Willow Creek Rd.<br>Riverton, Indiana 47000<br>555-214-7400<br>keystonestaffingservices.com</p>
    </div>
    <div class="program-title">
      <span class="name">KEYSTONE STAFFING</span>
      <span class="field">MEDICAL</span>
    </div>
  </section>

  <section class="panel panel--cover">
    <svg class="waves" viewBox="0 0 340 650" aria-hidden="true">
      <path d="M0 20 C110 35 240 30 340 5 L340 16 C240 42 110 46 0 32 Z" fill="var(--navy)"/>
      <path d="M0 250 C110 275 240 250 340 225 L340 405 C240 425 110 420 0 395 Z" fill="var(--blue)"/>
      <path d="M0 246 C110 270 240 246 340 220 L340 232 C240 258 110 282 0 258 Z" fill="var(--navy)"/>
    </svg>
    <div class="photo photo--team" role="img" aria-label="Photo of a team of doctors and nurses in white coats"></div>
    <p class="tagline">Providing high quality healthcare professionals</p>
    <div class="brand">
      <span class="brand-mark"></span>
      <span class="brand-name">Keystone<br>Staffing<br>Services</span>
    </div>
  </section>

</main>
</body>
</html>
```